Wedding Startup Full Website Design

We've just completed our online platform and need to create a website that represents our brand and vision, and clearly communicates our features and value proposition to potential users. There are a minimum of 4 pages that need to be designed. One geared toward wedding professionals (venues/vendors/coordinators), another toward engaged couples, one showcasing features, and an 'About Us' page.

The designer will creative freedom to create a unique UI/UX as long as it represents our brand and is relevant to our target audience/market. The ideal candidate will be able to assume the mindset of someone working in the wedding industry and/or an engaged couple. Ability to create illustrations is a plus.

Copy will be provided as needed. We will reimburse for stock images (pending approval before purchasing), but sourcing the stock images will be the responsibility of the designer.

Our current website: https://www.trelmora.com
Updates

Our project has now been guaranteed! We look forward to finding the perfect design for our site pages!

Still waiting for a design that stands out from the rest and aligns with the creative brief.

Target Market(s)

Wedding Professionals and Engaged Couples

Industry/Entity Type

Wedding

Number of Pages Required

4 page

Font styles to use
Sans Serif

Colors
ffffff
fbd4d5
f59195
33a6d7
cadf82
86cfc6

Requirements
Must have
• Common sense stuff like having a unified brand that accurately represents our platform, speaks to our target market, and clearly articulates our vision
Nice to have
• Illustrations
Should not have
• Overly cheesy or childish. We want to be professional but still embrace the wedding culture.

```html
<!DOCTYPE html>
<html lang="en">
<head>
<meta charset="utf-8">
<title>Trelmora — About Us</title>
<link href="https://fonts.googleapis.com/css2?family=Montserrat:wght@400;500&display=swap" rel="stylesheet">
<style>
  :root {
    --white: #ffffff;
    --gold: #c6a35a;
    --gold-light: #d9bd7f;
    --panel: rgba(190, 162, 100, 0.82);
    --hair-deep: #b4602c;
    --hair-light: #e39a5c;
    --backdrop: #e6d6b8;
    --backdrop-warm: #d8c3a0;
  }
  * { margin: 0; padding: 0; box-sizing: border-box; }
  html, body { width: 1200px; height: 674px; overflow: hidden; }
  body { font-family: "Montserrat", Arial, sans-serif; background: var(--backdrop); }
  .page { position: relative; width: 1200px; height: 674px; overflow: hidden; }

  .hero-photo {
    position: absolute; inset: 0;
    background:
      radial-gradient(ellipse 420px 360px at 330px 360px, var(--hair-light) 0%, var(--hair-deep) 55%, rgba(180,96,44,0) 78%),
      radial-gradient(ellipse 260px 180px at 500px 180px, rgba(255,255,255,0.55), rgba(255,255,255,0) 70%),
      linear-gradient(90deg, #a9603a 0%, #c98a5a 40%, var(--backdrop-warm) 68%, var(--backdrop) 100%);
  }

  .brand {
    position: absolute; left: 62px; top: 26px;
    display: flex; align-items: center; gap: 8px;
    color: var(--white); font-size: 30px; font-weight: 500; letter-spacing: 0.5px;
  }
  .brand-mark { width: 14px; height: 14px; border: 2px solid var(--gold-light); }

  .section-index { position: absolute; left: 1118px; top: 0; height: 142px; border-left: 2px solid var(--white); }
  .section-index .active-bar { position: absolute; left: -2px; top: 52px; width: 2px; height: 28px; background: var(--gold); }
  .section-index span { position: absolute; left: 8px; font-size: 13px; color: var(--white); }
  .section-index .is-active { color: var(--gold); font-size: 15px; font-weight: 500; }

  .vision { position: absolute; left: 811px; top: 100px; width: 300px; color: var(--gold); }
  .vision-title { display: inline-block; color: var(--white); font-size: 15px; padding-bottom: 2px; border-bottom: 2px solid var(--white); }
  .value { position: absolute; left: 0; width: 280px; }
  .value h3 { font-size: 14.5px; font-weight: 500; letter-spacing: 0.3px; }
  .value p { font-size: 12px; line-height: 15px; }
  .value-inspire { top: 33px; } .value-inspire p { margin-top: 19px; }
  .value-enjoy { top: 115px; } .value-enjoy p { margin-top: 14px; }
  .value-grow { top: 213px; } .value-grow p { margin-top: 0; }

  .mission {
    position: absolute; left: 754px; top: 370px; width: 446px; height: 208px;
    background: var(--panel); color: var(--white); padding: 11px 0 0 57px;
  }
  .mission h2 { font-size: 18px; font-weight: 400; letter-spacing: 0.3px; }
  .mission p { width: 340px; font-size: 12px; line-height: 13.7px; margin-top: 12px; }
  .mission p + p { margin-top: 13px; }

  .main-nav { position: absolute; top: 618px; left: 815px; display: flex; gap: 37px; }
  .main-nav a { color: var(--white); text-decoration: none; font-size: 16px; font-weight: 500; padding-bottom: 2px; }
  .main-nav .current { border-bottom: 2px solid var(--gold); }

  .side-link {
    position: absolute; left: 56px; top: 526px; height: 130px;
    writing-mode: vertical-rl; transform: rotate(180deg);
    color: var(--white); font-size: 16px; font-weight: 500; text-align: right;
  }
  .side-rule { position: absolute; left: 73px; top: 560px; width: 2px; height: 114px; background: var(--gold); }
  .menu-icon { position: absolute; left: 107px; top: 620px; }
</style>
</head>
<body>
<div class="page">
  <div class="hero-photo" role="img" aria-label="Close-up of a bride's braided copper hair with a pearl-dotted birdcage veil against a soft beige backdrop"></div>

  <div class="brand"><span class="brand-mark"></span>Trelmora</div>

  <nav class="section-index" aria-label="Sections">
    <div class="active-bar"></div>
    <span style="top:24px">01</span>
    <span class="is-active" style="top:57px">02</span>
    <span style="top:95px">03</span>
    <span style="top:129px">04</span>
  </nav>

  <section class="vision">
    <h2 class="vision-title">Our Vision</h2>
    <div class="value value-inspire"><h3>INSPIRE</h3><p>Inspire innovation and bringing dream weddings to life.</p></div>
    <div class="value value-enjoy"><h3>ENJOY</h3><p>For wedding professions and couples to enjoy the wedding planning experience.</p></div>
    <div class="value value-grow"><h3>GROW</h3><p>Foster growth for our partners and</p></div>
  </section>

  <section class="mission">
    <h2>Mission Statement</h2>
    <p>Weddings are one the most memorable events in people's life. Unfortunately planning a wedding is filled with stress, often leaving wedding professionals and their clients with soured memories.</p>
    <p>Our vision at Trelmora is to revamp the way weddings are planned on both sides of the process (wedding professionals and their clients). We aim to reduce the stress of everyone involved, and make the engagement season and wedding day memorable for the right reasons.</p>
  </section>

  <nav class="main-nav" aria-label="Main">
    <a class="current" href="#">About Us</a>
    <a href="#">Features</a>
    <a href="#">For Couples</a>
  </nav>

  <div class="side-rule"></div>
  <div class="side-link">Advisory Board</div>
  <svg class="menu-icon" width="17" height="13" viewBox="0 0 17 13" aria-label="Menu">
    <g stroke="#ffffff" stroke-width="1.6"><line x1="0" y1="1" x2="17" y2="1"/><line x1="0" y1="6.5" x2="17" y2="6.5"/><line x1="0" y1="12" x2="17" y2="12"/></g>
  </svg>
</div>
</body>
</html>
```